Need Trifold Brochure

I need a trifold brochure asap for a project.

Please KNOW how to do a trifold brochure. It should be an 8 1/2 x 11 brochure that is folded in thirds. So there are ultimately 6 sections, 3 on the front and 3 on the back. We need content on both sides, not just one. If you aren't sure what a trifold is please google it. If you submit a design that is not a true trifold it will be immediately eliminated.

All content located on this page
http://harborviewcosmeticclinic.example/
All text on this page needs to be incorporated.

Also I attached the 3 before and after images. All 3 of these need to be incorporated preferable\y on the inside of the trifold on per page. The very BACK of the trifold doesn't have to have content, other than maybe the company and phone.

On the outside of the trifold (not the inside) you could do a muted sea or ocean scape as long as the text is legible.

Same colors as website.
Updates

Target Market(s)

See website. This is for face lifts, so mostly women age 40 and over.

Industry/Entity Type

It Company

Requirements
Must have
• All content located on this page

Also I attached the 3 before and after images. When the trifold is open these could be on each of the 3 pages of the trifold, preferably at the top.

Same colors as website.

```html
<!DOCTYPE html>
<html lang="en">
<head>
<meta charset="utf-8">
<title>Harborview Cosmetic Clinic – Trifold Inside</title>
<link href="https://fonts.googleapis.com/css2?family=Crimson+Text:wght@600;700&family=Tinos:wght@700&family=Arimo:wght@400;700&display=swap" rel="stylesheet">
<style>
  :root {
    --ink-blue: #1d66a3;
    --ink-black: #111111;
    --paper: #ffffff;
    --sea-light: #e9f4f7;
    --sea-deep: #86c0d2;
  }
  html, body {
    margin: 0;
    padding: 0;
    width: 1200px;
    height: 927px;
    overflow: hidden;
    background: var(--paper);
  }
  .spread {
    position: relative;
    width: 1200px;
    height: 927px;
    background: linear-gradient(to bottom, var(--paper) 0, var(--paper) 775px, var(--sea-light) 805px, var(--sea-deep) 927px);
    font-family: "Crimson Text", Georgia, serif;
    overflow: hidden;
  }
  .case {
    position: absolute;
    top: 27px;
    width: 344px;
    margin: 0;
    padding: 0;
  }
  .case-photos {
    display: flex;
    height: 163px;
  }
  .case-photo {
    flex: 1;
  }
  .case-1 .before { background: linear-gradient(100deg, #d8d9de 0%, #c7a08c 45%, #d5d6da 100%); }
  .case-1 .after  { background: linear-gradient(100deg, #d9dade 0%, #3a2a26 35%, #c69a84 60%, #d6d7dc 100%); }
  .case-2 .before { background: linear-gradient(100deg, #8a6d52 0%, #c9a187 40%, #d4b08f 70%, #a48266 100%); }
  .case-2 .after  { background: linear-gradient(100deg, #c9b9a0 0%, #d6b198 45%, #e1c4a9 75%, #b79f86 100%); }
  .case-3 .before { background: linear-gradient(100deg, #2b2426 0%, #b88f80 45%, #cfd0d6 100%); }
  .case-3 .after  { background: linear-gradient(100deg, #2a2224 0%, #b78e7c 45%, #cdd0d8 100%); }
  .case-labels {
    display: flex;
    justify-content: space-between;
    font-family: "Arimo", Arial, sans-serif;
    font-weight: 700;
    font-size: 8px;
    color: var(--ink-black);
    margin-top: 3px;
  }
  .case-note {
    font-family: "Arimo", Arial, sans-serif;
    font-size: 7.5px;
    color: var(--ink-black);
    margin-top: 5px;
  }
  .case-note strong { font-size: 8px; }
  .case-1 { left: 30px; }
  .case-2 { left: 430px; }
  .case-3 { left: 830px; }

  .benefit {
    position: absolute;
    width: 400px;
    margin: 0;
    text-align: center;
    color: var(--ink-blue);
    font-weight: 700;
    font-size: 25px;
    line-height: 30px;
  }
  .benefit-large {
    font-size: 27px;
    line-height: 30px;
  }
  .col-1 { left: 0; }
  .col-2 { left: 400px; }
  .col-3 { left: 800px; }
  .benefit-note {
    display: block;
    font-weight: 600;
    font-size: 16.5px;
    line-height: 22px;
  }

  .tagline {
    position: absolute;
    top: 862px;
    margin: 0;
    width: 400px;
    text-align: center;
    font-family: "Tinos", "Times New Roman", serif;
    font-weight: 700;
    font-size: 31px;
    letter-spacing: -0.5px;
    color: var(--ink-black);
    transform: scaleX(0.92);
  }
  .disclaimer {
    position: absolute;
    top: 893px;
    right: 22px;
    font-family: "Tinos", "Times New Roman", serif;
    font-style: italic;
    font-size: 9px;
    color: var(--ink-black);
  }
</style>
</head>
<body>
<main class="spread">

  <figure class="case case-1">
    <div class="case-photos">
      <div class="case-photo before" role="img" aria-label="Patient profile before facelift"></div>
      <div class="case-photo after" role="img" aria-label="Patient profile after facelift"></div>
    </div>
    <div class="case-labels"><span>BEFORE</span><span>AFTER</span></div>
    <figcaption class="case-note"><strong>Actual Patient</strong> (patient also had optional neck lift procedure)</figcaption>
  </figure>

  <figure class="case case-2">
    <div class="case-photos">
      <div class="case-photo before" role="img" aria-label="Patient three-quarter view before facelift"></div>
      <div class="case-photo after" role="img" aria-label="Patient three-quarter view after facelift"></div>
    </div>
    <div class="case-labels"><span>BEFORE</span><span>AFTER</span></div>
    <figcaption class="case-note"><strong>Actual Patient</strong> (patient also had optional neck lift procedure)</figcaption>
  </figure>

  <figure class="case case-3">
    <div class="case-photos">
      <div class="case-photo before" role="img" aria-label="Patient profile before facelift"></div>
      <div class="case-photo after" role="img" aria-label="Patient profile after facelift"></div>
    </div>
    <div class="case-labels"><span>BEFORE</span><span>AFTER</span></div>
    <figcaption class="case-note"><strong>Actual Patient</strong> (patient also had optional neck lift procedure)</figcaption>
  </figure>

  <p class="benefit col-1" style="top:339px">No General Anesthesia<span class="benefit-note">(but available as an option if desired)</span></p>
  <p class="benefit col-1" style="top:437px">Decreased Risks</p>
  <p class="benefit col-1" style="top:546px">Less Scars</p>
  <p class="benefit col-1" style="top:655px">Very Quick Recovery*</p>

  <p class="benefit col-2" style="top:339px">Less Bruising and Swelling*</p>
  <p class="benefit col-2" style="top:416px">Significant Improvement*</p>
  <p class="benefit benefit-large col-2" style="top:499px">No Need for<br>Special Post-Op Care</p>
  <p class="benefit col-2" style="top:640px">Short Surgery Time</p>

  <p class="benefit col-3" style="top:339px">Free Consultation<br>With Our Staff</p>
  <p class="benefit benefit-large col-3" style="top:460px">Surgery performed by a fully<br>NBCS Board Certified,<br>internationally known,<br>plastic surgeon.</p>
  <p class="benefit benefit-large col-3" style="top:636px">Optional add-on procedures<br>can be done at the same time.</p>

  <p class="tagline col-1">THE NEW WAY TO</p>
  <p class="tagline col-2">LOOK AND FEEL</p>
  <p class="tagline col-3">BETTER FAST FOR LESS!</p>
  <span class="disclaimer">results may vary*</span>

</main>
</body>
</html>
```